Ventrel Advisory Inc. (Enterprise Resource Planning - All KORVA)

I need a logo and business card design for an ERP consulting company based in Dallas, We specifically provide consulting services for implementing and maintaining KORVA ERP systems, I would like to see all the colors be navy and white. White Card on one side with Navy print, and Navy card on the other side with White print. The design should communicate that we "Ventrel" results by effort, skill and courage.

Target Market(s)

Pinnacle 400 companies that are implementing or maintaining an KORVA ERP system. My specialty is Finance and Controlling

Industry/Entity Type

Business Consultant

Contact Information for Business Card

Dana Welby
President / CEO

3820 Brinlow Lane
Prosper, Texas 75291

Tel: 214-555-0187
eMail: dana.welby@ventreladvisory.example
web: www.ventreladvisory.example

Logo Text

This needs to be a Graphic Design

Font styles to use
Sans Serif

Colors
0555a3
ffffff

Requirements
Must have
• two sided
• Front side - Navy card with white print
• name, title, telephone, email
• Back side - White card with navy print
• street address, web address,
• Slogan [Ventrel ~ Drive, Craft, and Resolve}
Nice to have
• Classic and Clean
Should not have
• typical IT stuff... we are a consulting service organization not an IT department.

```html
<!DOCTYPE html>
<html lang="en">
<head>
<meta charset="utf-8">
<title>Ventrel Advisory Inc. — Business Card</title>
<link rel="stylesheet" href="https://fonts.googleapis.com/css2?family=Fira+Sans:wght@400;500&display=swap">
<style>
  :root {
    --navy: #0555a3;
    --white: #ffffff;
    --paper: #f3f3f3;
    --ink-soft: #3a6fb5;
    --backdrop: #9c9c9c;
  }
  * { box-sizing: border-box; margin: 0; padding: 0; }
  html, body {
    width: 1200px; height: 1200px; overflow: hidden;
    background: var(--backdrop);
    font-family: "Fira Sans", sans-serif;
  }
  .stage {
    width: 1200px; height: 1200px;
    display: flex; flex-direction: column; align-items: center; justify-content: center;
    gap: 70px;
  }
  .card {
    position: relative;
    width: 760px; height: 434px;
  }
  .card--front { background: var(--navy); color: var(--white); }
  .card--back {
    background: var(--paper); color: var(--ink-soft);
    display: flex; flex-direction: column; align-items: center; justify-content: center;
    gap: 2px;
  }

  .brand {
    position: absolute; left: 56px; top: 170px;
  }
  .brand__name {
    display: flex; align-items: center; gap: 12px;
    font-size: 44px; font-weight: 500; letter-spacing: 0.5px; line-height: 1;
  }
  .brand__mark {
    width: 16px; height: 16px; background: var(--white);
  }
  .brand__company {
    margin-top: 10px; font-size: 24px; font-weight: 400;
  }
  .brand__slogan {
    margin-top: 8px; font-size: 11px; letter-spacing: 0.2px;
  }

  .person {
    position: absolute; right: 56px; top: 190px; text-align: right;
  }
  .person__name { font-size: 34px; font-weight: 500; line-height: 1.1; }
  .person__title { font-size: 20px; }

  .divider {
    position: absolute; left: 56px; right: 56px; top: 318px;
    height: 1px; background: var(--white); opacity: 0.85;
  }
  .contact {
    position: absolute; right: 56px; top: 334px; text-align: right;
    font-size: 22px; line-height: 1.35;
  }

  .back__web { font-size: 30px; font-weight: 500; }
  .back__address { font-size: 22px; }
</style>
</head>
<body>
<main class="stage">
  <section class="card card--front" aria-label="Front of business card">
    <div class="brand">
      <div class="brand__name"><span class="brand__mark"></span>Ventrel</div>
      <div class="brand__company">Ventrel Advisory, Inc.</div>
      <div class="brand__slogan">Ventrel - Drive, Craft, and Resolve</div>
    </div>
    <div class="person">
      <div class="person__name">Dana Welby</div>
      <div class="person__title">President / CEO</div>
    </div>
    <div class="divider"></div>
    <div class="contact">
      <div>Tel: 214-555-0187</div>
      <div>eMail: dana.welby@ventreladvisory.example</div>
    </div>
  </section>

  <section class="card card--back" aria-label="Back of business card">
    <div class="back__web">www.ventreladvisory.example</div>
    <div class="back__address">3820 Brinlow Lane Larkfield, Ostreva 75291</div>
  </section>
</main>
</body>
</html>
```